Product label design needed for an odor removal line of products.

I need a label designed for an odor removal product line. There are eight additional odor removal products that I will need labels designed for so the winner will have additional work from me. I would like each of those products to have a similar look and feel in each one. This contest is for one of the products. The Breezeward Pod 385 (would love a better name if you are so inclined -many people know what it is by the 385). The no smell formula does not mask odors, it eliminates odors at their source . Also Reduces Allergens! Simply open silver packet and place in dispenser. Great for use in cars, near pet beds or litter boxes, near diaper pails -anywhere odors are a problem. Lasts 60-90 days. Safe to use. Other uses: Nursing homes, hotel rooms, locker rooms, teenage boy rooms, basements... Eco Friendly! No VOC's or phthalates! Do not consume. Keep out of reach of children and pets. Replace every 60-90 days. I put the picture of my logo , the product as it is packaged and a picture of the actual product and the dispenser it will go in. the package is 4x5 in silver packet with .25 seam on the side and .5 seam on the top and bottom. (Dispenser will have a label with reorder information on it. to be designed later) You do not have to put all information provided on the label. It is to be used as you see fit. I tend to like clean, bold designs but am open to all options. Prefer not to use word air freshener.

Target Market(s)

Men and women between 30-65

Industry/Entity Type

Cleaning Product

Font styles to use
Sans Serif

Colors
acd136
9bcb3c
ffffff

Requirements
Must have
• ability for concept/look to be used for a laundry product, smaller odor elimination pouch, odor removing canister and spray as well
Nice to have
• I like greens but am open to designers to decide
Should not have
• word air freshener

```html
<!DOCTYPE html>
<html lang="en">
<head>
<meta charset="utf-8">
<title>Breezeward Pod 385 – Label Front and Back</title>
<link rel="stylesheet" href="https://fonts.googleapis.com/css2?family=Montserrat:wght@400;600;800;900&family=Roboto+Condensed:wght@400;700&display=swap">
<style>
  :root{
    --lime:#acd136;
    --leaf:#9bcb3c;
    --forest:#3f8f2f;
    --deep:#2e6b24;
    --white:#ffffff;
    --stage:#e4e5e6;
    --ink:#4a4d50;
    --mist:#8a8d90;
    --band:#d9dadb;
  }
  *{box-sizing:border-box;margin:0;padding:0}
  html,body{width:870px;height:1200px;overflow:hidden}
  body{background:var(--stage);font-family:"Montserrat",sans-serif;color:var(--ink);position:relative}

  .label{position:absolute;top:360px;width:390px;height:440px;background:var(--white);border-radius:26px;overflow:hidden;box-shadow:0 2px 6px rgba(0,0,0,.12)}
  .label--front{left:30px}
  .label--back{left:450px}
  .caption{position:absolute;top:830px;width:390px;text-align:center;font-size:13px;letter-spacing:6px;color:var(--mist);font-weight:600}
  .caption--front{left:30px}
  .caption--back{left:450px}

  .swoosh{position:absolute;left:0;right:0;top:0;height:190px;
    background:linear-gradient(160deg,rgba(172,209,54,.05) 10%,rgba(172,209,54,.45) 45%,rgba(155,203,60,.15) 70%,rgba(255,255,255,0) 90%)}

  .brand{position:absolute;display:flex;align-items:center;gap:7px;white-space:nowrap}
  .brand__dot{width:22px;height:22px;border-radius:50%;background:var(--forest)}
  .brand__name{font-weight:800;font-size:13px;color:var(--forest);letter-spacing:.5px}
  .label--front .brand{top:24px;left:50%;transform:translateX(-50%)}
  .label--back .brand{right:22px;bottom:18px}

  .title{position:absolute;left:0;right:0;text-align:center}
  .label--front .title{top:100px}
  .title__main{font-weight:900;font-size:42px;line-height:1;color:var(--leaf);letter-spacing:-1px;white-space:nowrap}
  .title__sub{display:flex;align-items:center;justify-content:center;gap:8px;margin-top:6px;font-weight:900;font-size:36px;color:var(--forest);line-height:1}
  .badge-num{display:inline-flex;align-items:center;justify-content:center;width:50px;height:50px;border-radius:50%;background:var(--leaf);color:var(--white);font-size:18px;font-weight:800;border:3px solid var(--white);box-shadow:0 0 0 2px var(--leaf)}

  .front-band{position:absolute;left:0;right:0;top:236px;height:30px;background:var(--band);display:flex;align-items:center;justify-content:center;font-weight:800;font-size:13px;letter-spacing:3px;color:var(--ink)}
  .front-tag{position:absolute;top:276px;left:0;right:0;text-align:center;font-size:12px;font-weight:600;color:var(--forest);letter-spacing:1px}
  .icons{position:absolute;left:28px;top:316px;display:flex;gap:12px}
  .icons span{width:36px;height:36px;border-radius:50%;background:var(--ink);color:var(--white);font-size:8px;font-weight:700;display:flex;align-items:center;justify-content:center;text-align:center;line-height:1.1}
  .front-note{position:absolute;right:26px;top:318px;width:150px;font-family:"Roboto Condensed",sans-serif;font-size:10px;line-height:1.35;color:var(--mist);text-align:right}
  .front-foot{position:absolute;left:0;right:0;bottom:0;height:44px;background:var(--leaf);display:flex;align-items:center;justify-content:center;color:var(--white);font-weight:700;font-size:11px;letter-spacing:2px}

  .label--back .swoosh{height:150px}
  .back-title{position:absolute;left:22px;top:50px;width:190px}
  .back-title .title__main{font-size:22px;text-align:left;letter-spacing:-.5px}
  .back-title .title__sub{justify-content:flex-start;font-size:20px}
  .back-title .badge-num{width:32px;height:32px;font-size:11px;border-width:2px}
  .section-head{font-weight:800;font-size:11px;letter-spacing:1.5px;color:var(--forest);margin-bottom:6px}
  .back-copy{position:absolute;left:22px;top:148px;width:178px}
  .back-copy p{font-family:"Roboto Condensed",sans-serif;font-size:10.5px;line-height:1.4;color:var(--ink);margin-bottom:8px}
  .checks{position:absolute;left:226px;top:60px;width:146px}
  .checks ul{list-style:none}
  .checks li{display:flex;align-items:center;gap:7px;font-family:"Roboto Condensed",sans-serif;font-size:10.5px;color:var(--ink);margin-bottom:10px}
  .checks svg{flex:none}
  .back-rule{position:absolute;left:22px;right:22px;bottom:70px;height:2px;background:var(--leaf)}
  .phone{position:absolute;left:22px;bottom:26px;display:flex;align-items:center;gap:8px;font-weight:800;font-size:15px;color:var(--forest);white-space:nowrap}
  .warn{position:absolute;left:22px;bottom:82px;font-family:"Roboto Condensed",sans-serif;font-size:9.5px;color:var(--mist);width:340px}
</style>
</head>
<body>
  <section class="label label--front" aria-label="Front label">
    <div class="swoosh" role="img" aria-label="Soft green flowing wave decoration"></div>
    <div class="brand"><span class="brand__dot"></span><span class="brand__name">FERNHOLLOW LABS</span></div>
    <div class="title">
      <div class="title__main">BREEZEWARD</div>
      <div class="title__sub">POD <span class="badge-num">385</span></div>
    </div>
    <div class="front-band">DO NOT CONSUME</div>
    <div class="front-tag">ELIMINATES ODORS AT THEIR SOURCE</div>
    <div class="icons"><span>ECO<br>SAFE</span><span>NO<br>VOC</span><span>60-90<br>DAYS</span></div>
    <p class="front-note">No smell formula that removes odors and reduces allergens. Simply open and place in dispenser.</p>
    <div class="front-foot">KEEP OUT OF REACH OF CHILDREN</div>
  </section>
  <div class="caption caption--front">FRONT</div>

  <section class="label label--back" aria-label="Back label">
    <div class="swoosh" role="img" aria-label="Soft green flowing wave decoration"></div>
    <div class="back-title">
      <div class="title__main">BREEZEWARD</div>
      <div class="title__sub">POD <span class="badge-num">385</span></div>
    </div>
    <div class="back-copy">
      <div class="section-head">NO SMELL FORMULA</div>
      <p>Does not mask odors, it eliminates them at their source and also reduces allergens.</p>
      <p>Simply open the silver packet and place it in the dispenser. Replace every 60-90 days.</p>
    </div>
    <div class="checks">
      <div class="section-head">GREAT FOR USE IN</div>
      <ul>
        <li><svg width="14" height="14" viewBox="0 0 14 14"><rect width="14" height="14" rx="2" fill="#9bcb3c"/><path d="M3 7.5l2.5 2.5L11 4.5" stroke="#fff" stroke-width="2" fill="none"/></svg>Cars and garages</li>
        <li><svg width="14" height="14" viewBox="0 0 14 14"><rect width="14" height="14" rx="2" fill="#9bcb3c"/><path d="M3 7.5l2.5 2.5L11 4.5" stroke="#fff" stroke-width="2" fill="none"/></svg>Pet beds and litter boxes</li>
        <li><svg width="14" height="14" viewBox="0 0 14 14"><rect width="14" height="14" rx="2" fill="#9bcb3c"/><path d="M3 7.5l2.5 2.5L11 4.5" stroke="#fff" stroke-width="2" fill="none"/></svg>Diaper pails</li>
        <li><svg width="14" height="14" viewBox="0 0 14 14"><rect width="14" height="14" rx="2" fill="#9bcb3c"/><path d="M3 7.5l2.5 2.5L11 4.5" stroke="#fff" stroke-width="2" fill="none"/></svg>Locker rooms</li>
        <li><svg width="14" height="14" viewBox="0 0 14 14"><rect width="14" height="14" rx="2" fill="#9bcb3c"/><path d="M3 7.5l2.5 2.5L11 4.5" stroke="#fff" stroke-width="2" fill="none"/></svg>Basements</li>
      </ul>
    </div>
    <p class="warn">Do not consume. Keep out of reach of children and pets. No VOC's or phthalates.</p>
    <div class="back-rule"></div>
    <div class="phone">
      <svg width="18" height="18" viewBox="0 0 24 24" aria-hidden="true"><path fill="#3f8f2f" d="M6.6 10.8a15.1 15.1 0 006.6 6.6l2.2-2.2a1 1 0 011-.25 11.4 11.4 0 003.6.57 1 1 0 011 1V20a1 1 0 01-1 1A17 17 0 013 4a1 1 0 011-1h3.5a1 1 0 011 1 11.4 11.4 0 00.57 3.6 1 1 0 01-.25 1z"/></svg>
      303-555-0184
    </div>
    <div class="brand"><span class="brand__dot"></span><span class="brand__name">FERNHOLLOW LABS</span></div>
  </section>
  <div class="caption caption--back">BACK</div>
</body>
</html>
```